Supercar Dealership needs 2 web pages designed and a footer

Dear All,
We currently have a new company website being developed and we already have the majority of it sorted but there are a few pages and areas which either need creating or improving so I'm looking for some fresh design ideas that I can pass over to our web developers.

First of all I would like to focus on our 'Sell Your Car' page. I have included a design from our current web developer but I'm not happy with it. Although I like the general layout it just feels too basic and unappealing. I'm looking for a fresh design which brings this to life a bit and has a more attractive feel to it but mainly using the same content that is already in the design and one that fits in with the style and font of the Navigation bar at the top as I don't want to change this. But I'm sure you'll agree the design and detail of the page can be vastly improved.

The second web page that I would like to create is our 'Model Pages' which is basically a page which lists some information on a particular model for example a Velmont 612. We want to include a couple of paragraphs of text which describes the model, ideally one image of the model, an area where we can put a video of the model and then a list of previously sold and for sale cars of that model and all clearly titled. To give you an idea we have this page on our current website but for the new website being developed I'm looking for a fresh improved design which also incorporates an area for video. Please see link for current website: http://www.corvexmotorhaus.com/model/229/Velmont-612/for-sale Also don't worry about the right hand column for this as we no longer have this on new website.

The final part of the task is that I'm looking to create a brand new footer which incorporates some links, social media icons, maybe our opening hours and our logo. Again I have included what they have designed to give you an idea but I think the design is awful. I'm looking for something classy, professional and cool and a big improvement on what the current web developer has designed.

Target Market(s)

Males
25 - 75 years old
Wealthy Customers AB

Industry/Entity Type

Automotive

Number of Pages Required

2 page

Colors

Designer to choose colors to be used in the design.

Requirements
Must have
• 1. Sell Your Car Page
• 2. Model Page
• 3. New Footer

```html
<!DOCTYPE html>
<html lang="en">
<head>
<meta charset="utf-8">
<title>Sell Your Car – Corvex Motorhaus</title>
<link href="https://fonts.googleapis.com/css2?family=Open+Sans:wght@300;400;600&display=swap" rel="stylesheet">
<style>
:root{
  --navy:#2f3e51;
  --navy-dark:#2b3a4c;
  --ink:#1f2630;
  --muted:#666b72;
  --line:#cfd3d8;
  --panel-grey:#efefef;
  --band-grey:#e9e9e9;
  --white:#ffffff;
  --footer-text:#d6dbe2;
}
*{box-sizing:border-box;margin:0;padding:0}
html,body{width:1200px;height:2679px;overflow:hidden;background:var(--white)}
body{font-family:"Open Sans",Arial,sans-serif;color:var(--ink);position:relative}

/* header */
.site-header{position:absolute;left:0;top:0;width:1200px;height:125px;background:var(--white)}
.brand{position:absolute;left:121px;top:44px;display:flex;align-items:center;gap:10px;font-size:24px;font-weight:400;color:var(--ink);line-height:1}
.brand-mark{width:26px;height:26px;border-radius:50%;background:var(--navy);display:block}
.social{position:absolute;display:flex;gap:8px}
.social span{width:30px;height:30px;border-radius:50%;background:var(--navy);display:flex;align-items:center;justify-content:center}
.social span::after{content:"";width:8px;height:8px;border-radius:50%;background:var(--white)}
.header-social{left:702px;top:24px}
.phone{position:absolute;left:908px;top:22px;font-size:22px;color:var(--ink);display:flex;align-items:center;gap:6px}
.main-nav{position:absolute;left:346px;top:76px;display:flex;gap:22px;font-size:14px;color:#333;text-transform:uppercase}
.main-nav a{color:inherit;text-decoration:none}
.main-nav .current{color:var(--ink)}

/* hero */
.hero{position:absolute;left:0;top:125px;width:1200px;height:361px;
  background:linear-gradient(180deg,#5f6872 0%,#2a2f36 55%,#1a1d22 100%)}
.hero-title{position:absolute;left:0;top:282px;width:1200px;text-align:center;color:var(--white);font-size:37px;font-weight:600}

/* intro */
.tagline{position:absolute;left:0;top:530px;width:1200px;text-align:center;font-size:31px;font-weight:400;letter-spacing:1px;line-height:40px;color:var(--ink)}
.intro{position:absolute;left:180px;top:626px;width:840px;text-align:center;font-size:14px;line-height:24px;color:var(--muted)}

/* option panels */
.option{position:absolute;top:834px;width:477px;height:309px;padding:100px 36px 0;text-align:center}
.option h3{font-size:23px;font-weight:400;margin-bottom:12px}
.option p{font-size:12px;line-height:18px}
.option-dark{left:118px;background:var(--navy);color:var(--white)}
.option-light{left:605px;background:var(--panel-grey);border:1px solid #c9cdd1;color:var(--ink)}
.option-light p{color:var(--muted)}
.option-badge{position:absolute;top:780px;width:108px;height:108px;border-radius:50%;background:var(--white);border:1px solid #d4d7db;display:flex;align-items:center;justify-content:center}

/* forward orders band */
.forward{position:absolute;left:0;top:1175px;width:1200px;height:366px;
  background:linear-gradient(120deg,#4a4d54 0%,#2b2d33 45%,#1d2230 100%)}
.forward h2{position:absolute;left:0;top:102px;width:1200px;text-align:center;color:var(--white);font-size:31px;font-weight:400}
.forward p{position:absolute;left:140px;top:156px;width:920px;text-align:center;color:#e6e8ec;font-size:13.5px;line-height:26px}

/* form */
.form-heading{position:absolute;left:0;width:1200px;text-align:center;font-size:25px;font-weight:400;color:var(--ink)}
.form-heading::after{content:"";display:block;width:180px;height:1px;background:var(--line);margin:8px auto 0}
.field{position:absolute;height:46px;border:1px solid var(--line);background:var(--white);font-size:13px;color:#555;padding:14px 16px}
.textarea{height:100px}
.contact-label{position:absolute;left:130px;top:2069px;font-size:18px;color:#444}
.select{position:absolute;left:354px;top:2058px;width:355px;height:46px;border:1px solid var(--line);font-size:15px;color:#444;padding:12px 18px}
.select svg{position:absolute;right:18px;top:17px}
.submit{position:absolute;left:725px;top:2058px;width:354px;height:46px;background:var(--navy);color:var(--white);font-size:21px;text-align:center;line-height:46px;letter-spacing:1px}

/* newsletter */
.newsletter{position:absolute;left:0;top:2175px;width:1200px;height:92px;background:var(--band-grey)}
.newsletter-label{position:absolute;left:172px;top:31px;font-size:22px;color:var(--ink)}
.newsletter-input{position:absolute;left:402px;top:24px;width:424px;height:44px;background:var(--white);font-size:13px;color:#999;padding:13px 16px 0 44px}
.newsletter-input svg{position:absolute;left:16px;top:15px}
.newsletter-btn{position:absolute;left:826px;top:24px;width:161px;height:44px;background:var(--navy);color:var(--white);font-size:18px;text-align:center;line-height:44px}

/* footer */
.site-footer{position:absolute;left:0;top:2267px;width:1200px;height:412px;background:var(--navy-dark);color:var(--footer-text)}
.footer-brand{position:absolute;left:123px;top:86px;display:flex;align-items:center;gap:10px;font-size:22px;font-weight:400;color:#c9d0d8;line-height:1}
.footer-brand .brand-mark{background:#c9d0d8;width:24px;height:24px}
.footer-motto{position:absolute;left:123px;top:138px;font-size:16px;color:#c9d0d8}
.footer-col{position:absolute;top:60px}
.footer-col h4{font-size:21px;font-weight:400;color:var(--white);margin-bottom:14px}
.footer-col li{list-style:none;font-size:14.5px;line-height:28px}
.hours li{font-size:14px}
.footer-social{left:854px;top:197px}
.footer-social span{background:transparent;border:2px solid var(--white);width:33px;height:33px}
.footer-rule{position:absolute;left:118px;top:340px;width:964px;height:1px;background:#4b5a6c}
.copyright{position:absolute;left:0;top:362px;width:1200px;text-align:center;font-size:11px;color:#b3bcc7}
</style>
</head>
<body>

<header class="site-header">
  <div class="brand"><span class="brand-mark"></span>Corvex Motorhaus</div>
  <div class="social header-social"><span></span><span></span><span></span><span></span><span></span></div>
  <div class="phone">
    <svg width="18" height="18" viewBox="0 0 24 24"><path fill="#1f2630" d="M6.6 10.8a15.1 15.1 0 0 0 6.6 6.6l2.2-2.2c.3-.3.7-.4 1-.2 1.1.4 2.3.6 3.6.6.6 0 1 .4 1 1V20c0 .6-.4 1-1 1A17 17 0 0 1 3 4c0-.6.4-1 1-1h3.5c.6 0 1 .4 1 1 0 1.3.2 2.5.6 3.6.1.3 0 .7-.2 1z"/></svg>
    01632 960 418
  </div>
  <nav class="main-nav">
    <a class="current">Home</a><a>Current Stock</a><a>Sell Your Car</a><a>Finance</a><a>Vehicle Scourcing</a><a>About Us</a><a>Contact Us</a>
  </nav>
</header>

<section class="hero" role="img" aria-label="Row of parked luxury cars at dusk"></section>
<h1 class="hero-title">SELL YOUR CAR</h1>

<h2 class="tagline">TOP PRICES PAID . NATIONWIDE COLLECTION .<br>IMMEDIATE PAYMENT . HASSLE FREE</h2>
<p class="intro">Corvex Motorhaus are widely acknowledged as one of the UK's leading buyers of luxury and performance cars.<br>We are always looking to buy new stock and using our experience and knowledge of the market our aim is to make selling your car as simple and convenient as possible.<br>Only cars of the highest calibre similar to our stock list will be considered for an outright purchase with a strong preference for later models, low mileage with full service history. There are a few different options when it comes to selling your car</p>

<div class="option option-dark">
  <h3>Part-Exchange</h3>
  <p>The most convenient way of buying a new car is undoubtedly by offering your current car in part-exchange and very often is the best way to strike a good deal.<br>Though we always prefer to part-exchange a car we can sell on ourselves we can part-exchange any car and due to our fantastic relationships with a network of dealerships we will ensure we get the very best price for your car.</p>
</div>
<div class="option option-light">
  <h3>Sale or Return</h3>
  <p>Believe your car is worth more than what you've been offered? Thinking of selling privately?<br>It's always worth considering our brokerage service which will ensure you the maximum return for your car avoiding the risks and hassle of selling your car privately. By selling the car on your behalf we can offer more flexibility and you will benefit from having your car prepared to the extremely high standards of Corvex and advertised across</p>
</div>
<div class="option-badge" style="left:303px">
  <svg width="54" height="54" viewBox="0 0 54 54"><circle cx="27" cy="27" r="25" fill="#2f3e51"/><g fill="none" stroke="#fff" stroke-width="3"><circle cx="27" cy="27" r="11"/><circle cx="27" cy="27" r="4"/></g><g stroke="#fff" stroke-width="4"><path d="M27 11v5M27 38v5M11 27h5M38 27h5M15.7 15.7l3.5 3.5M34.8 34.8l3.5 3.5M15.7 38.3l3.5-3.5M34.8 19.2l3.5-3.5"/></g></svg>
</div>
<div class="option-badge" style="left:789px">
  <svg width="46" height="40" viewBox="0 0 46 40"><path fill="#2f3e51" d="M28 2l16 15-16 15v-9C16 23 8 27 2 38 4 23 12 12 28 11z"/></svg>
</div>

<section class="forward" role="img" aria-label="Close-up of a dark sports car front at sunset">
  <h2>Forward Orders</h2>
  <p>Put down a deposit on a new car you no longer want? Want to see if there is a small premium to be made on a highly demanded car?<br>We may well buy the contract from you or sell it on for you hassle free. Just get in touch.<br>If any of these options interest you or if you want more details then please call us. Alternatively complete the form below and we will get back to you as soon as possible with our best price.</p>
</section>

<h3 class="form-heading" style="top:1596px">Personal Details</h3>
<div class="field" style="left:118px;top:1665px;width:236px">Name</div>
<div class="field" style="left:361px;top:1665px;width:236px">Email</div>
<div class="field" style="left:605px;top:1665px;width:236px">Phone</div>
<div class="field" style="left:848px;top:1665px;width:236px">Post Code</div>

<h3 class="form-heading" style="top:1748px">Vehicle Details</h3>
<div class="field" style="left:116px;top:1820px;width:314px">Make</div>
<div class="field" style="left:444px;top:1820px;width:315px">Model</div>
<div class="field" style="left:768px;top:1820px;width:316px">Registration</div>
<div class="field" style="left:116px;top:1875px;width:314px">Mileage</div>
<div class="field" style="left:444px;top:1875px;width:315px">Exterior Colour</div>
<div class="field" style="left:768px;top:1875px;width:316px">Interior Colour</div>
<div class="field textarea" style="left:116px;top:1936px;width:968px">Please provide any useful information such as specification and service history</div>

<div class="contact-label">Preference of Contact</div>
<div class="select">Phone
  <svg width="16" height="10" viewBox="0 0 16 10"><path d="M1 1l7 7 7-7" fill="none" stroke="#555" stroke-width="1.6"/></svg>
</div>
<div class="submit">SUBMIT</div>

<section class="newsletter">
  <div class="newsletter-label">Latest Stock Updates</div>
  <div class="newsletter-input">
    <svg width="18" height="13" viewBox="0 0 18 13"><rect x="0.5" y="0.5" width="17" height="12" fill="none" stroke="#999"/><path d="M1 1l8 6 8-6" fill="none" stroke="#999"/></svg>
    Email address
  </div>
  <div class="newsletter-btn">Subscribe</div>
</section>

<footer class="site-footer">
  <div class="footer-brand"><span class="brand-mark"></span>Corvex Motorhaus</div>
  <div class="footer-motto">PASSIONATE ABOUT PERFORMANCE</div>
  <div class="footer-col" style="left:446px">
    <h4>COMPANY</h4>
    <ul><li>Home</li><li>Stock</li><li>Sell Your Car</li><li>Finance &amp; Insurance</li></ul>
  </div>
  <div class="footer-col" style="left:661px">
    <h4>RESOURCES</h4>
    <ul><li>Source Me a Car</li><li>About Us</li><li>Contact Us</li></ul>
  </div>
  <div class="footer-col hours" style="left:854px;top:54px">
    <h4>OPENING HOURS</h4>
    <ul><li>Mon to Fri: 09:00 - 18:00</li><li>Saturday: 09:00 - 17:00</li><li>Sunday by Appointment only</li></ul>
  </div>
  <div class="social footer-social"><span></span><span></span><span></span><span></span><span></span></div>
  <div class="footer-rule"></div>
  <div class="copyright">© 2017 Company Name&nbsp; All right reserved&nbsp; Term of Use</div>
</footer>

</body>
</html>
```